Stationery Design Project for Wellmind Therapy Institute

I would like you to design a letterhead and appt cards and letterhead. i have attached our current brochure so that you can see the kind of clinic that we are - for some context.

Generally our letters will go to General Practitioners.
Appt cards to clients. The text can stay the same as current documents as attached but the design obviously needs to be totally changed.

We are a psychology clinic with several psychologists that work for me. THe psychologists come and go so I am not wanting to list their names on the stationary.

In terms of letterhead my name (dr marianne pelko) needs to be on there..eg dr marianne pelko & associates.

With envelopes we need to be discrete therefore we simply have WTI & our address.

Everything goes under the banner of Wellmind Therapy Institute Pty Ltd.

I would like it to be consistent in theme/colours with the logo you designed and our website which has just gone live www.wellmindtherapyinstitute.com.au

Target Market(s)

General practitioners, potential referrers usually in the medical/health field,

Industry/Entity Type

Clinic

Requirements
Must have
• Logo

Address Suite 4, 2187 Farrowby Rd, Tillermont West 3172
P 9563 2814 F 9563 2816 E info@wellmindtherapyinstitute.com.au
W wellmindtherapyinstitute.com.au

Wellmind Therapy Institute Pty Ltd (small font)
ABN (ill need to provide this) (small font)
Nice to have
• I really like in my website how the colours are graded in the banners...I think this gives a softer feel...so if something like that would look good in our stationary then please use that kind of technique too...but you guys are the experts.

```html
<!DOCTYPE html>
<html lang="en">
<head>
<meta charset="utf-8">
<title>Wellmind Therapy Institute — Letterhead</title>
<link rel="stylesheet" href="https://fonts.googleapis.com/css2?family=Lato:wght@400;700&display=swap">
<style>
  :root {
    --backdrop: #ececec;
    --paper: #ffffff;
    --ink: #5a5a5a;
    --ink-soft: #6b6b6b;
    --brand-teal: #9fd3d5;
    --tone-light: #bfe2e2;
    --tone-mid: #8cc5c8;
    --tone-deep: #5e928d;
  }
  * { margin: 0; padding: 0; box-sizing: border-box; }
  html, body {
    width: 1200px;
    height: 900px;
    overflow: hidden;
    background: var(--backdrop);
    font-family: "Lato", sans-serif;
  }
  .letterhead {
    position: absolute;
    left: 290px;
    top: 12px;
    width: 620px;
    height: 876px;
    background: var(--paper);
  }
  .tone-band {
    position: absolute;
    left: 0;
    width: 100%;
    background: linear-gradient(90deg, var(--tone-light) 0%, var(--tone-mid) 50%, var(--tone-deep) 100%);
  }
  .tone-band--top { top: 0; height: 4px; }
  .tone-band--bottom { bottom: 0; height: 12px; }

  .brand {
    position: absolute;
    left: 65px;
    top: 36px;
    display: flex;
    align-items: center;
    gap: 15px;
  }
  .brand-dot {
    width: 50px;
    height: 50px;
    border-radius: 50%;
    background: var(--brand-teal);
  }
  .brand-name {
    font-size: 11px;
    font-weight: 400;
    letter-spacing: 2.6px;
    line-height: 13.5px;
    color: var(--ink-soft);
    text-transform: uppercase;
  }

  .footer {
    position: absolute;
    left: 45px;
    top: 819px;
    font-size: 8.6px;
    line-height: 11.5px;
    color: var(--ink);
    font-weight: 400;
  }
  .footer-col { position: absolute; top: 0; white-space: nowrap; }
  .footer-company { left: 0; }
  .footer-address { left: 161px; top: -1px; }
  .footer-phone { left: 299px; }
  .footer-web { left: 384px; }
  .footer-abn { font-size: 7.2px; }
  .phone-label { display: inline-block; width: 14px; font-weight: 700; }
</style>
</head>
<body>
  <main class="letterhead">
    <div class="tone-band tone-band--top"></div>

    <header class="brand">
      <div class="brand-dot"></div>
      <p class="brand-name">Wellmind<br>Therapy<br>Institute</p>
    </header>

    <footer class="footer">
      <div class="footer-col footer-company">
        Dr Marianne Pelko &amp; Associates<br>
        Wellmind Therapy Institute Pty Ltd<br>
        <span class="footer-abn">ABN 58 317 904 226</span>
      </div>
      <div class="footer-col footer-address">
        Suite 4, 2187 Farrowby Rd<br>
        Tillermont West 3172
      </div>
      <div class="footer-col footer-phone">
        <span class="phone-label">t</span>9563 2814<br>
        <span class="phone-label">f</span>9563 2816
      </div>
      <div class="footer-col footer-web">
        info@wellmindtherapyinstitute.com.au<br>
        wellmindtherapyinstitute.com.au
      </div>
    </footer>

    <div class="tone-band tone-band--bottom"></div>
  </main>
</body>
</html>
```